Biz Cards to match new logo

I'm looking for a business card layout to go with my new logo. I'd like to have one side in colour (purple, with the logo in white) and the other side to be white with the purple logo and contact info in black font: name, address (2 lines), phone, email, fax, website. The logo includes the company name so it doesn't need to be repeated in the text. The font should be legibile to the semi-blind. (I hate small fonts on business cards).

Industry/Entity Type

Business

```html
<!DOCTYPE html>
<html lang="en">
<head>
<meta charset="UTF-8">
<title>Orivale Studies – Business Card</title>
<link rel="stylesheet" href="https://fonts.googleapis.com/css2?family=Source+Sans+3:wght@400;600;700&display=swap">
<style>
  :root {
    --brand-purple: #4e1cc7;
    --rule-purple: #5a22d6;
    --mark-purple: #4a24c4;
    --ink: #111111;
    --paper: #ffffff;
  }
  html, body {
    margin: 0;
    padding: 0;
    width: 1200px;
    height: 702px;
    overflow: hidden;
    background: var(--paper);
  }
  .card {
    position: relative;
    width: 1200px;
    height: 702px;
    background: var(--paper);
    font-family: "Source Sans 3", "Myriad Pro", Arial, sans-serif;
    color: var(--ink);
  }
  .brand {
    position: absolute;
    left: 70px;
    top: 78px;
    width: 260px;
    text-align: center;
  }
  .brand-square {
    display: block;
    width: 64px;
    height: 64px;
    margin: 0 auto 18px;
    background: var(--mark-purple);
  }
  .brand-name {
    font-size: 34px;
    font-weight: 600;
    line-height: 1.1;
    color: var(--mark-purple);
    letter-spacing: 1px;
  }
  .divider {
    position: absolute;
    left: 353px;
    top: 66px;
    width: 4px;
    height: 166px;
    background: var(--rule-purple);
  }
  .identity {
    position: absolute;
    left: 400px;
    top: 110px;
    width: 362px;
    text-align: center;
  }
  .person-name {
    margin: 0;
    font-size: 42px;
    font-weight: 400;
    line-height: 1.15;
  }
  .person-role {
    margin: 2px 0 0;
    font-size: 37px;
    font-weight: 400;
    line-height: 1.15;
  }
  .contact-band {
    position: absolute;
    left: 0;
    top: 332px;
    width: 1200px;
    height: 370px;
    background: var(--brand-purple);
    color: var(--paper);
  }
  .contact-list {
    position: absolute;
    left: 0;
    top: 0;
    margin: 0;
    padding: 0;
    list-style: none;
    font-size: 33px;
    line-height: 1;
  }
  .contact-list li {
    position: absolute;
    white-space: nowrap;
  }
  .contact-list .label { font-weight: 700; }
  .contact-mobile { left: 69px; top: 35px; }
  .contact-fax    { left: 71px; top: 102px; }
  .contact-email  { left: 64px; top: 163px; }
  .contact-web    { left: 67px; top: 224px; }
  .address {
    position: absolute;
    left: 674px;
    top: 104px;
    width: 400px;
    margin: 0;
    text-align: center;
    font-style: normal;
    font-size: 39px;
    line-height: 50px;
  }
</style>
</head>
<body>
  <div class="card">
    <div class="brand">
      <span class="brand-square"></span>
      <div class="brand-name">ORIVALE STUDIES</div>
    </div>

    <div class="divider"></div>

    <div class="identity">
      <h1 class="person-name">Name Goes Here</h1>
      <p class="person-role">Designation</p>
    </div>

    <section class="contact-band">
      <ul class="contact-list">
        <li class="contact-mobile"><span class="label">Mobile&nbsp; No</span> : 000-000-0000</li>
        <li class="contact-fax"><span class="label">Fax No</span> : 0000-000-0000</li>
        <li class="contact-email"><span class="label">E-mail</span> : xyz@example.com</li>
        <li class="contact-web"><span class="label">Web</span> : www.example.com</li>
      </ul>
      <address class="address">Address Line 1<br>Address&nbsp; Line 2</address>
    </section>
  </div>
</body>
</html>
```